VORTA Diagnostics Pooling One Sheet

The process and concept for pooling is to target large populations of people; i.e. a school, prison, employer (where people are isolated by pods), then to test them all in one controllable group. By breaking down the pool size (ideally is 12 or 16 max) then when a positive pool pops up, the entity has the lab automatically reflex to test the whole pool to determine who is positive. During that exchange, several workflows could take place from the population that was being tested. This type of pooled testing is called Surveillance testing ,when it reflects, then it goes to Screening or Diagnostic testing.

The workflow is:
School/employer collects all patient information captured on a requisition form or electronically (w signature) and DOES NOT send to VORTA
School/employer collects individual specimens and labels them with a unique bar code (non-repeating and can include the DOB)
School/employer is responsible for housing and managing all the unique patient information for each individual specimen
School/employer delivers specimens to VORTA and School/employer directs VORTA what specimens are in what designated pool (one pool size for entire project)
When a pool is positive, VORTA notifies School/employer
When reflex testing in indicated for client, School/employer submits to VORTA on demand all patient information needed to process the reflexed option
VORTA reports back to School/employer in 12 hours the results of the retest
https://www.healthbureau-example.test/medical-devices/coronavirus-covid-19-and-medical-devices/pooled-sample-testing-and-screening-testing-covid-19
https://www.mediquestlabs.test/coronavirus-disease-covid-19/news/mediquest-receives-authorization-covid-19-sample-pooling

Target Market(s)

Schools, Universities, Employers

Font styles to use
Sans Serif

Colors
85acd3
85cae6
34a6d7

Requirements
Must have
• VORTA branded along with an elegant yet clinical feel. have all contact information for VORTA Diagnostics. Go to www.vortadx.test for all info

```html
<!DOCTYPE html>
<html lang="en">
<head>
<meta charset="utf-8">
<title>VORTA Diagnostics – Nursing Home COVID Testing</title>
<link href="https://fonts.googleapis.com/css2?family=Montserrat:wght@400;500;600;700;800&display=swap" rel="stylesheet">
<style>
  :root {
    --ink: #2b3e4c;
    --navy: #283d4b;
    --teal: #2aa9c3;
    --teal-deep: #1b5263;
    --accent: #34a6d7;
    --sky: #85cae6;
    --steel: #85acd3;
    --panel: #ebebed;
    --panel-line: #c9ccd0;
    --rule: #d4d7da;
    --white: #ffffff;
  }
  * { margin: 0; padding: 0; box-sizing: border-box; }
  html, body { width: 800px; height: 1200px; overflow: hidden; background: var(--white); }
  body { font-family: "Montserrat", sans-serif; color: var(--ink); }
  .sheet { position: relative; width: 800px; height: 1200px; overflow: hidden; background: var(--white); }

  .virus-mark { position: absolute; border-radius: 50%; background: radial-gradient(circle, #e2e4e7 0%, #eef0f2 55%, rgba(255,255,255,0) 72%); }

  .brand { position: absolute; left: 44px; top: 74px; display: flex; align-items: center; gap: 14px; }
  .brand-square { width: 52px; height: 52px; background: var(--navy); }
  .brand-name { font-weight: 600; font-size: 33px; color: var(--navy); letter-spacing: -0.3px; }

  .title-band { position: absolute; left: 0; top: 177px; width: 371px; height: 283px;
    background: linear-gradient(180deg, #2ab2c9 0%, #23889e 45%, #1c4f5f 100%); }
  .title { position: absolute; left: 46px; top: 50px; color: var(--white); font-weight: 800; font-size: 35px; line-height: 46px; letter-spacing: 0.6px; }
  .title-rule { position: absolute; left: 46px; top: 158px; width: 300px; height: 2px; background: rgba(255,255,255,0.9); }
  .title-rule::after { content: ""; position: absolute; left: 22px; top: -2px; width: 40px; height: 6px; background: var(--navy); }
  .subtitle { position: absolute; left: 47px; top: 194px; color: var(--white); font-size: 15px; line-height: 18px; font-weight: 400; }

  .hero { position: absolute; left: 0; top: 0; width: 800px; height: 620px; pointer-events: none; }

  .stats-panel { position: absolute; left: 404px; top: 438px; width: 372px; height: 356px; background: var(--panel); border: 1px solid var(--panel-line); }
  .figures { position: absolute; top: 622px; height: 72px; background: var(--navy); opacity: 0.85; border-radius: 3px; }
  .figures.pair { left: 448px; width: 88px; }
  .figures.five { left: 574px; width: 190px; }
  .stats-divider { position: absolute; left: 551px; top: 642px; width: 1px; height: 115px; background: #b9bdc2; }
  .stat { position: absolute; top: 711px; text-align: center; font-size: 13px; line-height: 16px; color: var(--ink); }
  .stat b { display: block; color: var(--teal); font-weight: 600; font-size: 13px; margin-bottom: 1px; }
  .stat.left { left: 418px; width: 130px; }
  .stat.right { left: 585px; width: 170px; }

  .section-head { position: absolute; left: 44px; font-size: 24px; font-weight: 400; color: var(--ink); letter-spacing: 0.3px; }
  .section-head strong { color: var(--teal); font-weight: 700; }
  .about-head { top: 481px; }
  .about-rule { position: absolute; left: 44px; top: 523px; width: 168px; height: 1px; background: var(--rule); }
  .workflow-head { top: 772px; }
  .workflow-rule { position: absolute; left: 44px; top: 816px; width: 30px; height: 3px; background: var(--navy); }

  .about-text { position: absolute; left: 44px; top: 547px; width: 333px; font-size: 13.1px; line-height: 16.3px; text-align: justify; color: var(--ink); }

  .steps { position: absolute; list-style: none; font-size: 13.2px; line-height: 16.3px; color: var(--ink); }
  .steps li { position: absolute; left: 0; padding-left: 24px; white-space: nowrap; }
  .steps li::before { content: ""; position: absolute; left: 1px; top: 3px; width: 9px; height: 9px; border: 2px solid var(--teal-deep); border-radius: 50%; }
  .steps.left-col { left: 52px; top: 0; }
  .steps.right-col { left: 446px; top: 0; }

  .footer-band { position: absolute; left: 0; bottom: 0; width: 800px; height: 82px; }
  .phone { position: absolute; left: 46px; top: 1138px; color: var(--white); font-weight: 700; font-size: 20px; display: flex; align-items: center; gap: 8px; letter-spacing: 0.3px; }
  .address { position: absolute; left: 46px; top: 1170px; color: var(--white); font-size: 13px; display: flex; align-items: center; gap: 8px; }
  .contact-line { position: absolute; left: 464px; top: 1152px; font-size: 14px; color: var(--ink); display: flex; align-items: center; gap: 6px; }
  .contact-line svg { flex: none; }
</style>
</head>
<body>
<main class="sheet">

  <div class="virus-mark" role="img" aria-label="Faint virus particle decoration" style="left:488px;top:4px;width:60px;height:60px;"></div>
  <div class="virus-mark" role="img" aria-label="Faint virus particle decoration" style="left:224px;top:470px;width:50px;height:50px;"></div>
  <div class="virus-mark" role="img" aria-label="Faint virus particle decoration" style="left:0;top:1066px;width:46px;height:46px;"></div>
  <div class="virus-mark" role="img" aria-label="Faint virus particle decoration" style="left:744px;top:1066px;width:56px;height:56px;"></div>

  <div class="brand">
    <span class="brand-square"></span>
    <span class="brand-name">VORTA Diagnostics</span>
  </div>

  <section class="title-band">
    <h1 class="title">NURSING HOME<br>COVID TESTING</h1>
    <div class="title-rule"></div>
    <p class="subtitle">POOLED SAMPLE TESTING AND<br>SCREENING TESTING FOR COVID-19</p>
  </section>

  <div class="stats-panel"></div>

  <svg class="hero" viewBox="0 0 800 620" aria-hidden="false">
    <defs>
      <linearGradient id="labPhoto" x1="0" y1="0" x2="1" y2="1">
        <stop offset="0" stop-color="#a9b6d8"/>
        <stop offset="0.45" stop-color="#5a6fa8"/>
        <stop offset="1" stop-color="#2f3f78"/>
      </linearGradient>
    </defs>
    <g fill="none" stroke="#283d4b" stroke-width="11" stroke-linecap="butt">
      <line x1="319" y1="153" x2="560" y2="74"/>
      <line x1="614" y1="40" x2="805" y2="148"/>
      <line x1="377" y1="177" x2="377" y2="454"/>
      <line x1="311" y1="488" x2="560" y2="569"/>
      <line x1="612" y1="604" x2="805" y2="494"/>
    </g>
    <polygon points="613,63 830,183 830,460 613,580 400,460 400,183" fill="url(#labPhoto)" role="img" aria-label="Photo of laboratory scientists in masks and goggles working at a microscope, with virus particles overlaid"/>
  </svg>

  <div class="figures pair" role="img" aria-label="Two female figure pictograms"></div>
  <div class="figures five" role="img" aria-label="Five male figure pictograms"></div>
  <div class="stats-divider"></div>
  <p class="stat left"><b>1 OUT OF 2</b>Women experience<br>UTI in their lifetime</p>
  <p class="stat right"><b>20%</b>Of diagnose UTI<br>patients are men</p>

  <h2 class="section-head about-head">ABOUT <strong>US</strong></h2>
  <div class="about-rule"></div>
  <p class="about-text">The process and concept for pooling is to target large populations of people; i.e. a school, prison, employer (where people are isolated by pods), then to test them all in one controllable group. By breaking down the pool size (ideally is 12 or 16 max) then when a positive pool pops up, the entity has the lab automatically reflex to test the whole pool to determine who is positive. During that exchange, several workflows could take place from the population that was being tested. This type of pooled testing is called Surveillance testing, when it reflects, then it goes to Screening or Diagnostic testing.</p>

  <h2 class="section-head workflow-head">THE <strong>WORKFLOW IS:</strong></h2>
  <div class="workflow-rule"></div>

  <ul class="steps left-col">
    <li style="top:850px;">School/employer collects all patient<br>information captured on a requisition form or<br>electronically (w signature) and DOES NOT<br>send to VORTA</li>
    <li style="top:932px;">School/employer collects individual specimens<br>and labels them with a unique bar code<br>(non-repeating and can include the DOB)</li>
    <li style="top:998px;">School/employer is responsible for housing<br>and managing all the unique patient<br>information for each individual specimen</li>
    <li style="top:1064px;">School/employer delivers specimens to VORTA and School/employer directs VORTA what specimens are in<br>what designated pool (one pool size for entire project)</li>
  </ul>
  <ul class="steps right-col">
    <li style="top:850px;">When a pool is positive, VORTA notifies<br>School/employer</li>
    <li style="top:899px;">When reflex testing in indicated for client,<br>School/employer submits to VORTA on demand<br>all patient information needed to process the<br>reflexed option</li>
    <li style="top:981px;">VORTA reports back to School/employer in 12<br>hours the results of the retest</li>
  </ul>

  <svg class="footer-band" viewBox="0 0 800 82" aria-hidden="true">
    <polygon points="0,2 371,2 438,82 0,82" fill="#283d4b"/>
    <rect x="430" y="66" width="370" height="8" fill="#2aa9c3"/>
  </svg>

  <p class="phone">
    <svg width="14" height="14" viewBox="0 0 24 24" aria-hidden="true"><path fill="#34a6d7" d="M6.6 10.8a15.1 15.1 0 0 0 6.6 6.6l2.2-2.2a1 1 0 0 1 1-.25 11.4 11.4 0 0 0 3.6.6 1 1 0 0 1 1 1V20a1 1 0 0 1-1 1A17 17 0 0 1 3 4a1 1 0 0 1 1-1h3.5a1 1 0 0 1 1 1c0 1.25.2 2.45.6 3.6a1 1 0 0 1-.25 1z"/></svg>
    555-010-VORT (8678)
  </p>
  <p class="address">
    <svg width="12" height="15" viewBox="0 0 24 30" aria-hidden="true"><path fill="#34a6d7" d="M12 0a10 10 0 0 0-10 10c0 7.5 10 20 10 20s10-12.5 10-20A10 10 0 0 0 12 0zm0 14a4 4 0 1 1 0-8 4 4 0 0 1 0 8z"/></svg>
    1200 Harbor Lane Suite I Springfield, ST 00000
  </p>
  <p class="contact-line">
    <svg width="13" height="10" viewBox="0 0 26 20" aria-hidden="true"><rect x="1" y="1" width="24" height="18" fill="none" stroke="#34a6d7" stroke-width="2"/><path d="M1 1l12 10L25 1" fill="none" stroke="#34a6d7" stroke-width="2"/></svg>
    info@vortadx.test
    <svg width="11" height="11" viewBox="0 0 24 24" aria-hidden="true" style="margin-left:6px"><circle cx="12" cy="12" r="10" fill="none" stroke="#34a6d7" stroke-width="3"/><path d="M2 12h20M12 2c4 4 4 16 0 20M12 2c-4 4-4 16 0 20" fill="none" stroke="#34a6d7" stroke-width="2"/></svg>
    www.vortadx.test
  </p>

</main>
</body>
</html>
```